Business Card Design Project used as hotel key

I need a project to be printed on PVC card and used by our customers as room key.

The design and the color are up to you. My idea would be to include the logo (colour can also be changed) on the front side and our Internet address on the back (http://www.kestravolin.ch, info@kestravolin.ch).

Target Market(s)

Hôtel customers

Industry/Entity Type

Hotel

Requirements
Must have
• I have attached below the template of the front and back of the card. The logo on the back shown on the template below the magnetic stripe should not be used.

Must have:

1. Follow the template size (shown in the template):

Full Bleed Size:
3.55" x 2.3"
90.17mm x 58.42mm
1065 x 690 pixels

Trim Size:
3.375" x 2.125"
85.77mm x 54.02mm
1013 x 638 pixels

A bleed is the outer area of your artwork that falls on the outside of the trim line. It is important that you do not have any important information in the bleed area as ¼ “ will be cut off on all sides. Cards with a “framed border” are not recommended due to variances in die cutting.

2. Make sure you leave the area between the magstripe markers on the template blank.

3. There need to be an arrow on the front side (on the left), pointing the left side

4. Color: Full color both sides, color process CMYK. 300 DPI at 100% of the final print size

```html
<!DOCTYPE html>
<html lang="fr">
<head>
<meta charset="utf-8">
<title>Hôtel Kestravolin – Room Key Card</title>
<link href="https://fonts.googleapis.com/css2?family=Oswald:wght@300;600&display=swap" rel="stylesheet">
<style>
  :root {
    --backdrop: #e6e2cc;
    --backdrop-low: #b9b7a8;
    --card-top: #a1475f;
    --card-bottom: #5b2b3b;
    --ink: #3a2018;
    --band: #45281d;
    --arrow: #dc8ea3;
    --stripe: #0b0b0b;
  }
  * { margin: 0; padding: 0; box-sizing: border-box; }
  html, body { width: 1200px; height: 797px; overflow: hidden; }
  body {
    background: linear-gradient(180deg, var(--backdrop) 0%, var(--backdrop-low) 100%);
    font-family: "Oswald", sans-serif;
    position: relative;
  }
  .key-card {
    position: absolute;
    top: 235px;
    width: 520px;
    height: 327px;
    border-radius: 14px;
    overflow: hidden;
    background: linear-gradient(160deg, var(--card-top) 0%, var(--card-bottom) 100%);
    box-shadow: 0 18px 40px rgba(40, 30, 20, 0.35);
  }
  .key-card--back { left: 55px; }
  .key-card--front { left: 625px; }

  /* back */
  .magstripe {
    position: absolute;
    left: 0; right: 0;
    top: 48px;
    height: 40px;
    background: var(--stripe);
  }
  .back-name {
    position: absolute;
    top: 150px;
    width: 100%;
    text-align: center;
    font-weight: 600;
    font-size: 26px;
    letter-spacing: 1px;
    color: var(--ink);
    text-transform: uppercase;
  }
  .contact {
    position: absolute;
    top: 232px;
    width: 100%;
    text-align: center;
    font-weight: 300;
    font-size: 12px;
    line-height: 16px;
    color: var(--ink);
  }

  /* front */
  .side-band {
    position: absolute;
    top: 0; bottom: 0;
    left: 42px;
    width: 26px;
    background: var(--band);
  }
  .side-rule {
    position: absolute;
    top: 0; bottom: 0;
    left: 88px;
    width: 4px;
    background: var(--band);
  }
  .entry-arrow {
    position: absolute;
    left: 48px;
    top: 138px;
    width: 40px;
    height: 52px;
  }
  .front-name {
    position: absolute;
    left: 120px;
    right: 20px;
    top: 138px;
    text-align: center;
    font-weight: 600;
    font-size: 40px;
    line-height: 52px;
    letter-spacing: 1px;
    color: var(--ink);
    text-transform: uppercase;
  }
</style>
</head>
<body>
  <section class="key-card key-card--back" aria-label="Verso de la carte">
    <div class="magstripe"></div>
    <p class="back-name">Hôtel Kestravolin</p>
    <p class="contact">info@kestravolin.ch<br>http://www.kestravolin.ch</p>
  </section>

  <section class="key-card key-card--front" aria-label="Recto de la carte">
    <div class="side-band"></div>
    <div class="side-rule"></div>
    <svg class="entry-arrow" viewBox="0 0 40 52" aria-hidden="true">
      <polygon points="0,26 40,0 40,52" fill="var(--arrow)"/>
    </svg>
    <p class="front-name">Hôtel Kestravolin</p>
  </section>
</body>
</html>
```